Tarrow Creek plumbing plumbing company business card design

Something sinilar to business card i upload it is my old business card design
And have a good watermark with the logo or majority of the logot in rhe background as watermark

Plumbing business similar to uploaded design with a nice watermark of the logo

Font styles to use
Script

Colors

Designer to choose colors to be used in the design.

```html
<!DOCTYPE html>
<html lang="en">
<head>
<meta charset="utf-8">
<title>Tarrow Creek Plumbing – Business Card</title>
<link rel="stylesheet" href="https://fonts.googleapis.com/css2?family=Montserrat:wght@400;500;600;700&display=swap">
<style>
  :root {
    --stage: #141517;
    --card: #232629;
    --card-band: #2c2f33;
    --watermark: #303337;
    --brand-blue: #1a7fd0;
    --text-white: #f2f4f6;
  }
  * { box-sizing: border-box; margin: 0; padding: 0; }
  html, body {
    width: 1200px; height: 800px; overflow: hidden;
    background: var(--stage);
    font-family: "Montserrat", Arial, sans-serif;
  }
  .canvas {
    position: relative; width: 1200px; height: 800px;
    display: flex; align-items: center; justify-content: center; gap: 40px;
  }
  .card {
    position: relative; width: 525px; height: 300px;
    background: var(--card); border-radius: 4px; overflow: hidden;
    box-shadow: 0 14px 40px rgba(0,0,0,.5);
  }
  .watermark-area { position: absolute; background: var(--watermark); }
  .card-front .watermark-area {
    left: 0; bottom: 0; width: 230px; height: 160px;
    border-top-right-radius: 70px;
  }
  .card-back .watermark-area {
    left: 0; top: 90px; width: 300px; height: 210px;
    border-top-right-radius: 80px;
  }
  .card-back .footer-band {
    position: absolute; left: 0; bottom: 0; width: 100%; height: 66px;
    background: var(--card-band);
  }
  .card-back .logo-panel {
    position: absolute; left: 34px; bottom: 18px; width: 240px; height: 120px;
    background: var(--card); border-radius: 0 22px 0 22px;
  }
  .brand-name {
    position: absolute; display: flex; align-items: center; gap: 10px;
    color: var(--text-white); font-weight: 700; letter-spacing: .04em;
    text-transform: uppercase; line-height: 1.1;
  }
  .brand-mark {
    width: 14px; height: 14px; border-radius: 50%; background: var(--brand-blue); flex: none;
  }
  .card-front .brand-name { left: 250px; top: 80px; font-size: 22px; }
  .card-back .brand-name { left: 54px; bottom: 52px; font-size: 19px; }
  .web-address {
    position: absolute; right: 36px; bottom: 36px;
    color: var(--text-white); font-size: 13px; letter-spacing: .16em; font-weight: 500;
  }
  .web-address .accent { color: var(--brand-blue); }
  .contact-block { position: absolute; right: 30px; top: 30px; width: 200px; }
  .person-name { color: var(--brand-blue); font-size: 20px; font-weight: 700; }
  .person-role { color: var(--text-white); font-size: 11px; margin-top: 2px; }
  .divider { height: 2px; background: var(--brand-blue); margin: 9px 0; }
  .address { color: var(--text-white); font-size: 11.5px; line-height: 1.45; font-weight: 500; }
  .contact-list { list-style: none; }
  .contact-list li {
    display: flex; align-items: center; gap: 7px;
    color: var(--text-white); font-size: 11.5px; line-height: 1.6; font-weight: 500;
  }
  .contact-list svg { width: 10px; height: 10px; fill: var(--brand-blue); flex: none; }
</style>
</head>
<body>
<main class="canvas">

  <section class="card card-front" aria-label="Business card front">
    <div class="watermark-area" role="img" aria-label="Faint large brand watermark"></div>
    <div class="brand-name"><span class="brand-mark"></span>Tarrow Creek<br>Plumbing</div>
    <p class="web-address">www.<span class="accent">tarrowcreekweb</span>.com</p>
  </section>

  <section class="card card-back" aria-label="Business card back">
    <div class="watermark-area" role="img" aria-label="Faint brand watermark"></div>
    <div class="footer-band"></div>
    <div class="logo-panel"></div>
    <div class="brand-name"><span class="brand-mark"></span>Tarrow Creek<br>Plumbing</div>

    <div class="contact-block">
      <h1 class="person-name">Dorian Maleki</h1>
      <p class="person-role">Director</p>
      <div class="divider"></div>
      <p class="address">PO BOX 123, your address<br>2nd street Halden</p>
      <div class="divider"></div>
      <ul class="contact-list">
        <li><svg viewBox="0 0 10 10"><path d="M2 0h2l1 3-1.5 1a6 6 0 0 0 2.5 2.5L7 5l3 1v2c0 1-1 2-2 2A8 8 0 0 1 0 2c0-1 1-2 2-2z"/></svg>0400 555 019</li>
        <li><svg viewBox="0 0 10 10"><path d="M0 2h10v1L5 6 0 3z M0 4.2l5 3 5-3V8H0z"/></svg>info@tarrowmail.com</li>
        <li><svg viewBox="0 0 10 10"><circle cx="5" cy="5" r="5"/></svg>www.tarrowcreekweb.com</li>
      </ul>
    </div>
  </section>

</main>
</body>
</html>
```